Lantern Keepers Lantern Scribes

We would like the business card to be Horizontal
Logo on the back and want it raised.

Target Market(s)

Education and Museums

Industry/Entity Type

Education

Contact Information for Business Card

Dolores Wrenfield, P.H.D.
3918 Pelham Rd
Fernhollow, OH 44799
612.447.3095
Dolores.Wrenfield@lanternkeeperslanternscribes.org
lanternkeeperslanternscribes.org

Font styles to use
Serif

Colors

Designer to choose colors to be used in the design.

Requirements
Must have
• letters and logo must be raised
• Must be slate blue card
• Silver is aluminum foil

```html
<!DOCTYPE html>
<html lang="en">
<head>
<meta charset="utf-8">
<title>Lantern Keepers Lantern Scribes – Business Card</title>
<link href="https://fonts.googleapis.com/css2?family=Lora:wght@600&family=Raleway:wght@400&family=Cormorant+Garamond:ital,wght@1,500&display=swap" rel="stylesheet">
<style>
  :root {
    --backdrop: #2b2c2e;
    --slate-dark: #53738f;
    --slate-light: #7190aa;
    --foil: #e4e8ec;
    --ink-white: #f7f9fb;
    --ghost: rgba(255, 255, 255, 0.13);
  }
  * { margin: 0; padding: 0; box-sizing: border-box; }
  html, body {
    width: 1200px;
    height: 1200px;
    overflow: hidden;
    background: var(--backdrop);
  }
  .sheet {
    width: 1200px;
    height: 1200px;
    display: flex;
    flex-direction: column;
    align-items: center;
    justify-content: center;
    gap: 44px;
  }
  .card {
    position: relative;
    width: 900px;
    height: 514px;
    background: linear-gradient(120deg, var(--slate-dark) 0%, var(--slate-light) 100%);
    overflow: hidden;
  }

  /* Front */
  .card--front {
    display: flex;
    flex-direction: column;
    align-items: center;
    justify-content: center;
    gap: 26px;
  }
  .brand-ring {
    width: 190px;
    height: 190px;
    border: 5px solid var(--foil);
    border-radius: 50%;
  }
  .brand-name {
    font-family: "Lora", serif;
    font-weight: 600;
    font-size: 34px;
    color: var(--foil);
    letter-spacing: 0.02em;
    white-space: nowrap;
  }

  /* Back: faint mark */
  .ghost-ring {
    position: absolute;
    left: 630px;
    top: 150px;
    width: 240px;
    height: 240px;
    border: 5px solid var(--ghost);
    border-radius: 50%;
  }
  .ghost-name {
    position: absolute;
    right: 26px;
    top: 42px;
    font-family: "Lora", serif;
    font-weight: 600;
    font-size: 22px;
    color: var(--ghost);
    letter-spacing: 0.02em;
    white-space: nowrap;
  }

  /* Back: contact block */
  .contact {
    position: absolute;
    left: 20px;
    top: 138px;
    width: 600px;
    text-align: center;
    color: var(--ink-white);
  }
  .contact__name {
    font-family: "Lora", serif;
    font-weight: 600;
    font-size: 38px;
    letter-spacing: 0.02em;
    margin-bottom: 12px;
    white-space: nowrap;
  }
  .contact__line {
    font-family: "Raleway", sans-serif;
    font-weight: 400;
    font-size: 19px;
    line-height: 32px;
    letter-spacing: 0.03em;
    white-space: nowrap;
  }
  .contact__tagline {
    font-family: "Cormorant Garamond", serif;
    font-style: italic;
    font-weight: 500;
    font-size: 25px;
    line-height: 31px;
    margin-top: 16px;
    white-space: nowrap;
  }
</style>
</head>
<body>
  <main class="sheet">
    <section class="card card--front" aria-label="Card front">
      <div class="brand-ring"></div>
      <div class="brand-name">Lantern Keepers Lantern Scribes</div>
    </section>

    <section class="card card--back" aria-label="Card back">
      <div class="ghost-name" aria-hidden="true">Lantern Keepers Lantern Scribes</div>
      <div class="ghost-ring" aria-hidden="true"></div>
      <div class="contact">
        <h1 class="contact__name">Dolores Wrenfield, Ph.D.</h1>
        <p class="contact__line">612.447.3095</p>
        <p class="contact__line">Dolores.Wrenfield@lanternkeeperslanternscribes.org</p>
        <p class="contact__line">www.lanternkeeperslanternscribes.org</p>
        <p class="contact__line">3918 Pelham Rd, Fernhollow, OH 44799</p>
        <p class="contact__tagline">Specializing in workshops and presentations on letters from<br>men in the United States Colored Troops</p>
      </div>
    </section>
  </main>
</body>
</html>
```